Startup incubator requires a funky cool brochure

please see design brief, please be creative but within the design confines listed in the corporatedesign pdf file

Industry/Entity Type

Startup

```html
<!DOCTYPE html>
<html lang="en">
<head>
<meta charset="utf-8">
<title>Nestbox Brochure Spread</title>
<link rel="stylesheet" href="https://fonts.googleapis.com/css2?family=Cinzel:wght@400&family=Arimo:wght@400;700&family=Raleway:wght@300;400&display=swap">
<style>
  :root {
    --backdrop: #2b2b2d;
    --amber: #f8b019;
    --charcoal: #2f3033;
    --paper: #ffffff;
    --ink: #2a2218;
    --body-grey: #4a4a4a;
    --band-text: #c9c9c9;
    --accent: #f1ac1c;
    --headline-grey: #7b7b7b;
  }
  * { box-sizing: border-box; margin: 0; padding: 0; }
  html, body { width: 1200px; height: 900px; overflow: hidden; background: var(--backdrop); }
  body { font-family: "Arimo", Arial, sans-serif; }

  .spread {
    position: absolute; left: 80px; top: 60px;
    width: 1040px; height: 780px;
    display: flex;
  }
  .page { position: relative; width: 520px; height: 780px; overflow: hidden; }
  .page__band {
    position: absolute; left: 0; right: 0; bottom: 0; height: 130px;
    background: var(--charcoal);
  }
  .page-number {
    position: absolute; bottom: 40px; font-size: 8px; color: var(--accent);
  }

  /* Left page */
  .page--letter { background: var(--amber); }
  .brand {
    position: absolute; top: 40px; left: 0; right: 0;
    display: flex; justify-content: center; align-items: center; gap: 6px;
  }
  .brand__square { width: 9px; height: 9px; background: var(--ink); }
  .brand__name {
    font-family: "Arimo", Arial, sans-serif; font-weight: 700;
    font-size: 14px; letter-spacing: 2px; color: var(--ink);
  }
  .section-title {
    font-family: "Cinzel", "Times New Roman", serif; font-weight: 400;
    font-size: 23px; letter-spacing: 1px;
  }
  .page--letter .section-title { position: absolute; top: 216px; left: 66px; color: var(--paper); }
  .letter {
    position: absolute; top: 258px; left: 66px; width: 410px;
    font-size: 7.6px; line-height: 11.2px; color: var(--ink);
  }
  .letter p { margin-bottom: 11px; }
  .page--letter .page-number { left: 66px; }

  /* Right page */
  .page--services { background: var(--paper); }
  .services-visual {
    position: absolute; top: 0; left: 288px; width: 172px; height: 190px;
    background: radial-gradient(ellipse at 50% 40%, #e9e9e9 0%, #a9a9a9 55%, #575757 100%);
  }
  .page--services .section-title { position: absolute; top: 216px; left: 72px; color: var(--accent); }
  .services-col {
    position: absolute; top: 262px; width: 190px;
    font-size: 7.8px; line-height: 11px; color: var(--body-grey);
  }
  .services-col p { margin-bottom: 12px; }
  .services-col--left { left: 72px; }
  .services-col--right { left: 290px; width: 188px; }
  .service-list {
    list-style: none; border-left: 1px solid var(--accent);
    padding-left: 10px; margin-left: -2px;
  }
  .service-list li { position: relative; padding-left: 10px; margin-bottom: 9px; }
  .service-list li::before {
    content: ""; position: absolute; left: 0; top: 3px;
    width: 4px; height: 4px; background: var(--body-grey);
  }
  .pull-quote {
    font-family: "Raleway", Arial, sans-serif; font-weight: 300;
    font-size: 12.5px; line-height: 15px; color: var(--headline-grey);
    text-transform: uppercase; letter-spacing: .3px;
  }
  .fee-note {
    position: absolute; top: 668px; width: 190px;
    font-size: 7.6px; line-height: 10.5px; color: var(--band-text);
  }
  .fee-note--left { left: 72px; }
  .fee-note--right { left: 290px; }
  .page--services .page-number { right: 36px; }
</style>
</head>
<body>
  <main class="spread">
    <section class="page page--letter">
      <div class="brand">
        <span class="brand__square"></span>
        <span class="brand__name">NESTBOX</span>
      </div>
      <h1 class="section-title">OPENING LETTER</h1>
      <div class="letter">
        <p>Starting Your Own Business Can Be Tough, There Are Challenges That Are Unforeseen, Limitations That You May Not Have Expected And Difficulties That You May Struggle To Face Alone. In This Delicate And Stressful Time Having The Right Partner Can Be Crucial To Your Success, And At Nestbox We Strive To Be That Partner, Helping Start-ups Through The Toughest Time Of Their Lives And Helping Them Mature Into Robust And Successful Businesses.</p>
        <p>Three Young Entrepreneurs, Much Like Yourself, Realized That Young Businesses Did Not Have The Support Or Space Which Would Otherwise Have Allowed Them To Succeed And Be Profitable. Samir El Haddad And Brothers Lukas &amp; Jonas Berger Decided To Create A Business With The Aim Of Optimizing Start-ups Prospects Of Success, A Space That Would Have Been Instrumental In Helping Them With Their Own Businesses.</p>
        <p>Samir, Currently A Business Developer With Vantor Industries Here In Dusseldorf, Maintains A Facility Management Business In The U.A.E, Whilst Jonas (Our Gm) Co-founded K.B.R With His Brother Lukas (Himself A 3 Year Veteran Of Domvest Gmbh – A Commercial And Residential Property Development Company In Dusseldorf), A Company Which Focuses On Property Development In Nrw.</p>
        <p>Nestbox Is An Incubator (Business Development) Service In Dusseldorf, Combining Free Operating Space And Professional Consultancy Services Specifically Designed To Nurture Young Businesses. Business Plans For Retail Companies Generally Require A Cost Designation Of 20% Of Annual Sales To Be Set Aside For Commercial Rental Costs, By Removing This Requirement And Providing Our Numerous Additional Services We Tangibly Reduce Your Risk And Give You A Helping Hand On Your Way To Establishing A Successful And Sustainable Business</p>
        <p>Our Vision Is To Promote Innovative Entrepreneurism In Dusseldorf By Discovering Interesting Businesses And Offering Them Services And Space On A No Rent/no Deposit Basis In Return For Remuneration Directly Based On Sales, With No Base Fees Or Hidden Costs. Our Journey Will Develop A Highly Networked Community Of Likeminded Entrepreneurs Operating In One Space And Offering Advice And Examples To Each Other In A Safer And Protected Environment.</p>
        <p>We believe that our business will become a strong asset for our partners in the growing entrepreneurial community in this city and we cannot wait to share our ideas with you!</p>
        <p>Best Regards,</p>
      </div>
      <div class="page__band"></div>
      <span class="page-number">1</span>
    </section>

    <section class="page page--services">
      <div class="services-visual" role="img" aria-label="Photo of a man in a tuxedo whose head is replaced by a cloud of sketched business icons, charts and strategy doodles"></div>
      <h2 class="section-title">SERVICES</h2>
      <div class="services-col services-col--left">
        <p>Nestbox Dusseldorf is prepared to provide your business with solutions that will mitigate the majority of overhead costs and initial investment costs that would normally be required to establish a retail business.</p>
        <p>Upon entering into an arrangement with us, we are committed to providing you with:</p>
        <ul class="service-list">
          <li>Shop/Display/Operating Space in a super-central, fashionable, high footfall location</li>
          <li>No Utility Costs (incl. gas, water, electricity and WiFi)</li>
          <li>Professional Meeting Rooms and Well Equipped Workspaces for Backroom Administration</li>
          <li>A communal ERP System with individualized accounts and settings.</li>
          <li>Business Development Advice (in-house)</li>
          <li>Free Seminars/Tutoring for various business administration skills from qualified professional staff (outsourced)</li>
          <li>A communal location attracting a wide range of otherwise unexposed customers</li>
        </ul>
      </div>
      <div class="services-col services-col--right">
        <p>Our goal is to help your business prove its concept, helping you to earn enough investment capital to establish your own stand-alone location, although if you want to stay for a while, we can certainly discuss it.</p>
        <p>The challenges in proving your concept can be daunting, sleepless nights watching your lifesavings are sunk into an unproven business or worse, feeling the weight of the repayments on the investment/start-up loans.</p>
        <p>The opportunity to determine whether your business is feasible in the marketplace with ZERO financial risk while at the same time earning the same margins and profits than you would in your very own store is an opportunity that sells itself.</p>
        <p>Whenever you feel comfortable ‘leaving the nest’ you will be in a much more confident position with your endeavor, and</p>
        <p class="pull-quote">The banks will certainly appreciate your proven concept when it comes determining your business’ credit-worthiness!</p>
      </div>
      <div class="page__band"></div>
      <p class="fee-note fee-note--left">Our all-inclusive remuneration will ultimately depend on the revenue you can generate. Nestbox will take a 15% service charge for the first $15,000 in sales per month. Should the business generate</p>
      <p class="fee-note fee-note--right">$15,000-$20,000 the service charge will drop to 10%, and any sales above $20,000 will only incur a 7.5% charge.</p>
      <span class="page-number">2</span>
    </section>
  </main>
</body>
</html>
```